Bi-Fold Brochure (Graphic and Color scheme only)

I need a front cover design and background colors for the other 3 panels. This brocher would be a folded 17X22 (four 8.5X11 panels). I have attached pictures of a similar brochure. I am alsoproviding examples of the color scheme and font color/design. I would like to have on additional piece of art included on the cover. We manufacture seating material for school buses so we would like a stylized, caricture style rendition of a school bus as the graphic on the front cover. The color of the bus graphic should match the font color on the example I have provided. I supplied a business card as an example. The background on the card is a brown leather. We would like to replicate that and the logo/font. After this graphic design is finished we need to be able to add text. I say that just to insure that we can import the project into a publishing software to complete the brochure. I have also included a couple of school bus image examples. These are not ideal but they give an example of the style of art we are looking for.

Industry/Entity Type

Graphic Design

Requirements
Must have
• Please notice the file attached named "KTR card source". This image shows the graphic design we desire- brown leather background, logo, font color. The only elements this design needs is four panels, all brown leather background, logo on front and a custom designed school bus image, green accent lines 1 inch from top and bottom of each page. The rest of the text for the brochure will be added later so the image needs to be formatted so it can be inserted into a publishing program to add text.
Should not have
• Should not have any additional design elements. This is a simple, clean design. The only custom design is a stylized school bus that matches the included font color (lime green)

```html
<!DOCTYPE html>
<html lang="en">
<head>
<meta charset="utf-8">
<title>KTR Brochure Front Cover</title>
<link rel="stylesheet" href="https://fonts.googleapis.com/css2?family=Josefin+Sans:wght@400;600;700&display=swap">
<style>
  :root {
    --canvas: #ffffff;
    --leather: #2b2725;
    --leather-light: #34302d;
    --lime-dark: #6a9632;
    --lime-light: #8cbd45;
    --logo-grey: #8d8d90;
    --tagline-green: #86b83f;
  }
  html, body {
    margin: 0;
    padding: 0;
    width: 1200px;
    height: 1000px;
    overflow: hidden;
    background: var(--canvas);
  }
  .canvas {
    position: relative;
    width: 1200px;
    height: 1000px;
  }
  .cover {
    position: absolute;
    left: 355px;
    top: 185px;
    width: 490px;
    height: 630px;
    background: radial-gradient(ellipse at 50% 45%, var(--leather-light), var(--leather) 70%);
    overflow: hidden;
  }
  .accent-band {
    position: absolute;
    left: 0;
    width: 100%;
    height: 56px;
    background: linear-gradient(90deg, var(--lime-dark) 0%, var(--lime-light) 50%, var(--lime-dark) 100%);
  }
  .accent-band--top { top: 0; }
  .accent-band--bottom { bottom: 0; }
  .bus-graphic {
    position: absolute;
    left: 108px;
    top: 190px;
    width: 265px;
    height: 165px;
    border-radius: 14px;
    background: linear-gradient(160deg, #7aab3a, #5b8a2a);
    opacity: 0.85;
  }
  .brand {
    position: absolute;
    left: 0;
    width: 100%;
    top: 388px;
    text-align: center;
    font-family: "Josefin Sans", sans-serif;
    font-weight: 700;
    font-size: 52px;
    letter-spacing: 4px;
    color: var(--logo-grey);
    margin: 0;
  }
  .tagline {
    position: absolute;
    left: 0;
    width: 100%;
    top: 456px;
    text-align: center;
    font-family: "Josefin Sans", sans-serif;
    font-weight: 600;
    font-size: 11px;
    letter-spacing: 1.4px;
    text-transform: uppercase;
    color: var(--tagline-green);
    margin: 0;
  }
</style>
</head>
<body>
  <main class="canvas">
    <section class="cover">
      <div class="accent-band accent-band--top"></div>
      <div class="bus-graphic" role="img" aria-label="Stylized caricature school bus illustration in lime green line art"></div>
      <h1 class="brand">KTR</h1>
      <p class="tagline">Keystone Transit Resources, LLC</p>
      <div class="accent-band accent-band--bottom"></div>
    </section>
  </main>
</body>
</html>
```